Photography business - business card design quick turn around

Create a business card design for me please. I actually need the final design back before the end of Sunday 13th May 7pm GMT. Sorry for the short notice.

Photoshop artwork template uploaded with artwork guidelines including printer profiles and other mandatory specifications. Only one side of the business card is required as the other side will be an image.

The design is required as an unflattened PSD file so that I can edit the text if I need to.

My brand colours are white and the teal you see in the logo. Occasionally I also use a dark grey on my website (I don't mind the shade of grey as appreciate grey on teal would be a different grey, to the grey I use on white on the website, so just use a shade of grey that matches). Font can be as the font for the logo or if you prefer I am open to another sans serif, easily legible font. Ideally font size will be 12+.Please do not use capital letters for text. I prefer everything to be lower case, if possible.

Thank you.

Nell

Target Market(s)

Other business owners who may refer me and families

Industry/Entity Type

Photographer

Contact Information for Business Card

Silver Kettle Photography Logo
Sub text: family portraiture, captured with love

Contact information, ideally using simple icons to represent email / website / facebook / instagram / pinterest

email: nell@silverkettlephotography.co.uk
website: silverkettlephotography.co.uk
facebook: @silverkettlephotography
pinterest: pinnedboards.net/silverkettlepho
instagram: @silverkettle_photography
mobile/telephone: 07931462097

If there is too much text then please drop the instagram and pinterest information.

Font styles to use
Sans Serif

Colors
33b8a4

Requirements
Must have
• Logo
• Contact details as listed above
• sub text
Nice to have
• Instagram and Pinterest contact details
• Nice to have icons to represent website / phone / facebook etc followered by the handle where relevant

```html
<!DOCTYPE html>
<html lang="en">
<head>
<meta charset="utf-8">
<title>Silver Kettle Photography – Business Card</title>
<link rel="stylesheet" href="https://fonts.googleapis.com/css2?family=Lato:wght@400;700&family=Questrial&display=swap">
<style>
  :root {
    --teal: #33b3a6;
    --teal-line: #8fd3cb;
    --grey: #8a8a8a;
    --card: #ffffff;
    --backdrop: #e9e7e4;
  }
  * { box-sizing: border-box; margin: 0; padding: 0; }
  html, body { width: 900px; height: 1200px; overflow: hidden; }
  body { background: var(--backdrop); position: relative; font-family: "Lato", sans-serif; }

  .card {
    position: absolute; left: 212px; top: 262px;
    width: 481px; height: 716px;
    background: var(--card); border-radius: 28px;
    box-shadow: 0 4px 14px rgba(0,0,0,0.12);
  }

  .brand {
    position: absolute; left: 46px; top: 90px;
    display: flex; align-items: center; gap: 14px;
  }
  .brand-mark { width: 52px; height: 52px; border-radius: 50%; background: var(--teal); flex: none; }
  .brand-name {
    font-family: "Lato", sans-serif; font-weight: 700;
    font-size: 25px; line-height: 1; color: var(--teal); white-space: nowrap;
  }

  .contacts { position: absolute; left: 0; top: 216px; width: 100%; list-style: none; }
  .contact { height: 61.5px; text-align: center; }
  .contact-divider { position: relative; height: 26px; }
  .contact-divider::before {
    content: ""; position: absolute; left: 133px; width: 214px; top: 13px;
    height: 1px; background: var(--teal-line);
  }
  .contact-icon {
    position: absolute; left: 227px; top: 0; width: 26px; height: 26px;
    border-radius: 50%; background: var(--teal);
    display: flex; align-items: center; justify-content: center;
  }
  .contact-icon svg { width: 14px; height: 14px; }
  .contact-text {
    display: block; margin-top: 5px; white-space: nowrap;
    font-size: 22.5px; line-height: 1.2; font-weight: 700; color: var(--teal); letter-spacing: 0.3px;
  }

  .tagline {
    position: absolute; left: 0; width: 100%; top: 645px; text-align: center;
    font-family: "Questrial", sans-serif; font-size: 21px; letter-spacing: 0.5px; color: var(--grey);
  }
</style>
</head>
<body>
  <main class="card">
    <div class="brand">
      <span class="brand-mark" aria-hidden="true"></span>
      <span class="brand-name">Silver Kettle Photography</span>
    </div>

    <ul class="contacts">
      <li class="contact">
        <div class="contact-divider"><span class="contact-icon">
          <svg viewBox="0 0 24 24"><path fill="#fff" d="M6.6 10.8a15.1 15.1 0 0 0 6.6 6.6l2.2-2.2c.3-.3.7-.4 1-.2 1.1.4 2.3.6 3.6.6.6 0 1 .4 1 1V20c0 .6-.4 1-1 1A17 17 0 0 1 3 4c0-.6.4-1 1-1h3.5c.6 0 1 .4 1 1 0 1.2.2 2.4.6 3.6.1.3 0 .7-.2 1z"/></svg>
        </span></div>
        <span class="contact-text">07931462097</span>
      </li>
      <li class="contact">
        <div class="contact-divider"><span class="contact-icon">
          <svg viewBox="0 0 24 24"><rect x="3" y="6" width="18" height="12" rx="1" fill="none" stroke="#fff" stroke-width="2"/><path d="M3 7l9 6 9-6" fill="none" stroke="#fff" stroke-width="2"/></svg>
        </span></div>
        <span class="contact-text">nell@silverkettlephotography.co.uk</span>
      </li>
      <li class="contact">
        <div class="contact-divider"><span class="contact-icon">
          <svg viewBox="0 0 24 24" fill="none" stroke="#fff" stroke-width="1.8"><circle cx="12" cy="12" r="9"/><ellipse cx="12" cy="12" rx="4" ry="9"/><path d="M3 12h18M5 7h14M5 17h14"/></svg>
        </span></div>
        <span class="contact-text">silverkettlephotography.co.uk</span>
      </li>
      <li class="contact">
        <div class="contact-divider"><span class="contact-icon" aria-hidden="true"></span></div>
        <span class="contact-text">@silverkettlephotography</span>
      </li>
      <li class="contact">
        <div class="contact-divider"><span class="contact-icon" aria-hidden="true"></span></div>
        <span class="contact-text">pinnedboards.net/silverkettlepho</span>
      </li>
      <li class="contact">
        <div class="contact-divider"><span class="contact-icon" aria-hidden="true"></span></div>
        <span class="contact-text">@silverkettle_photography</span>
      </li>
    </ul>

    <p class="tagline">family portraiture, captured with love</p>
  </main>
</body>
</html>
```